QR TILL WORKS , CREDIT CARD PROCESSING EQUIPMENT

qrtillworks is a sub division of Tallow a credit car processing co.
dorian vale
14 cedar hollow ln
alder falls ct 07312
suite 412

qrtillworks.example
cell 555-214-7730
office 555-861-2093
we sell pos systems to merchant who want to accept credit cards at there retail location.
black card would be nice buit open to different ideas

Target Market(s)

retail merchants

Industry/Entity Type

credit card processing

Contact Information for Business Card

card should include web site phone address

Colors

Designer to choose colors to be used in the design.

Requirements
Should not have
• red

```html
<!DOCTYPE html>
<html lang="en">
<head>
<meta charset="utf-8">
<title>QR Till Works – Business Card</title>
<link href="https://fonts.googleapis.com/css2?family=Montserrat:wght@400;700&display=swap" rel="stylesheet">
<style>
  :root {
    --bg: #3a3a3a;
    --card: #1a1a1a;
    --yellow: #f2c21b;
    --white: #f4f4f4;
  }
  * { margin: 0; padding: 0; box-sizing: border-box; }
  html, body { width: 1200px; height: 801px; overflow: hidden; }
  body {
    background: var(--bg);
    font-family: "Montserrat", sans-serif;
    position: relative;
  }
  .card {
    position: absolute;
    top: 252px;
    width: 520px;
    height: 297px;
    background: var(--card);
    border-bottom: 3px solid var(--yellow);
    box-shadow: 0 0 0 1px var(--yellow);
    overflow: hidden;
  }
  .card--front { left: 60px; }
  .card--back { left: 620px; }

  .brand {
    position: absolute;
    display: flex;
    align-items: center;
    gap: 10px;
  }
  .brand__mark {
    width: 14px; height: 14px;
    background: var(--yellow);
  }
  .brand__name {
    color: var(--white);
    font-weight: 400;
    font-size: 24px;
    letter-spacing: 0.5px;
    white-space: nowrap;
  }
  .card--front .brand { left: 36px; top: 112px; }

  .holder {
    position: absolute;
    right: 34px; top: 158px;
    color: var(--yellow);
    font-weight: 700;
    font-size: 17px;
    letter-spacing: 0.5px;
    text-transform: uppercase;
  }
  .divider {
    position: absolute;
    left: 36px; right: 34px; top: 188px;
    height: 1px;
    background: var(--yellow);
  }
  .contacts {
    position: absolute;
    left: 36px; top: 204px;
    list-style: none;
    color: var(--white);
    font-size: 12px;
    line-height: 20px;
  }
  .contacts li { display: flex; align-items: center; gap: 8px; }
  .contacts svg { width: 11px; height: 11px; flex: none; }
  .address {
    position: absolute;
    right: 34px; top: 204px;
    color: var(--white);
    font-size: 12px;
    line-height: 19px;
    text-align: right;
    font-style: normal;
  }

  .pattern {
    position: absolute;
    inset: 0;
    background: linear-gradient(160deg, #262626 0%, #151515 55%, #0e0e0e 100%);
  }
  .card--back .brand { left: 250px; top: 118px; }
</style>
</head>
<body>
  <section class="card card--front" aria-label="Business card front">
    <div class="brand">
      <span class="brand__mark"></span>
      <span class="brand__name">QR TILL WORKS</span>
    </div>
    <div class="holder">dorian vale</div>
    <div class="divider"></div>
    <ul class="contacts">
      <li>
        <svg viewBox="0 0 12 12"><rect x="3" y="0.5" width="6" height="11" rx="1" fill="none" stroke="var(--yellow)" stroke-width="1.3"/></svg>
        555-214-7730
      </li>
      <li>
        <svg viewBox="0 0 12 12"><path d="M2.5 1.5 L4.5 1 L5.5 3.8 L4.2 4.8 Q5.2 7 7.2 7.8 L8.2 6.5 L11 7.5 L10.5 9.5 Q5 10.5 1.5 4 Z" fill="var(--yellow)"/></svg>
        555-861-2093
      </li>
      <li>
        <svg viewBox="0 0 12 12"><circle cx="6" cy="6" r="5" fill="none" stroke="var(--yellow)" stroke-width="1.3"/><path d="M1 6 H11 M6 1 Q3 6 6 11 Q9 6 6 1" fill="none" stroke="var(--yellow)" stroke-width="1"/></svg>
        qrtillworks.example
      </li>
    </ul>
    <address class="address">
      14 cedar hollow ln<br>
      alder falls ct 07312<br>
      suite 412
    </address>
  </section>

  <section class="card card--back" aria-label="Business card back">
    <div class="pattern" role="img" aria-label="Subtle dark embossed monogram pattern covering the card"></div>
    <div class="brand">
      <span class="brand__mark"></span>
      <span class="brand__name">QR TILL WORKS</span>
    </div>
  </section>
</body>
</html>
```